International Consultancy Needs Slick Professional Presentation Graphic

Varnolt are an international engineering and advisory consultancy servicing the mining industry with a mix of Technology (Software), Services (consulting) and Systems (work structures).

We need a slick presentation graphic for use in presentation slides, whitepapers. I have attached a basic pic of the information we want to convey. Flat or 3D no preference, colouring no preference. Don't have to be circles, that was just easiest to draft up initially.

Industry/Entity Type

Mining

```html
<!DOCTYPE html>
<html lang="en">
<head>
<meta charset="utf-8">
<title>Varnolt Capability Model</title>
<link rel="stylesheet" href="https://fonts.googleapis.com/css2?family=Lato:wght@400;700;900&display=swap">
<style>
  :root {
    --bg-deep: #0b4394;
    --bg-light: #1c63c0;
    --ring: #ffffff;
    --tech: #2f7ad0;
    --tech-dark: #1b5cb0;
    --people: #3a4fae;
    --people-dark: #22348a;
    --systems: #2a73c6;
    --systems-dark: #1a5cad;
    --overlap-ui: #22b4e6;
    --overlap-sys: #1e98da;
    --overlap-org: #1fa6e0;
    --core-top: #9ccc44;
    --core-bottom: #0c9645;
    --label: #ffffff;
  }
  html, body {
    margin: 0;
    padding: 0;
    width: 1200px;
    height: 844px;
    overflow: hidden;
    background: var(--bg-deep);
  }
  .canvas {
    display: block;
    width: 1200px;
    height: 844px;
  }
  .label {
    font-family: "Lato", sans-serif;
    fill: var(--label);
    text-anchor: middle;
  }
  .label--domain { font-size: 20px; font-weight: 700; }
  .label--overlap { font-size: 15px; font-weight: 400; }
  .label--core { font-size: 24px; font-weight: 700; }
  .icon { fill: var(--label); stroke: none; }
  .icon-line { stroke: var(--label); stroke-width: 2; fill: none; }
</style>
</head>
<body>
<svg class="canvas" viewBox="0 0 1200 844" xmlns="http://www.w3.org/2000/svg" aria-labelledby="diagram-title">
  <title id="diagram-title">Capability sits where Technology, People and Systems meet</title>
  <defs>
    <linearGradient id="bg-gradient" x1="0" y1="0" x2="1" y2="1">
      <stop offset="0" stop-color="var(--bg-deep)"/>
      <stop offset="1" stop-color="var(--bg-light)"/>
    </linearGradient>
    <linearGradient id="circuit-wash" x1="0" y1="0" x2="0" y2="1">
      <stop offset="0" stop-color="#5a8fd8" stop-opacity="0.35"/>
      <stop offset="1" stop-color="#5a8fd8" stop-opacity="0"/>
    </linearGradient>
    <linearGradient id="tech-fill" x1="0" y1="0" x2="1" y2="1">
      <stop offset="0" stop-color="var(--tech)"/>
      <stop offset="1" stop-color="var(--tech-dark)"/>
    </linearGradient>
    <linearGradient id="people-fill" x1="0" y1="0" x2="1" y2="1">
      <stop offset="0" stop-color="var(--people)"/>
      <stop offset="1" stop-color="var(--people-dark)"/>
    </linearGradient>
    <linearGradient id="systems-fill" x1="0" y1="0" x2="1" y2="1">
      <stop offset="0" stop-color="var(--systems-dark)"/>
      <stop offset="1" stop-color="var(--systems)"/>
    </linearGradient>
    <linearGradient id="core-fill" x1="0" y1="0" x2="0" y2="1">
      <stop offset="0" stop-color="var(--core-top)"/>
      <stop offset="1" stop-color="var(--core-bottom)"/>
    </linearGradient>
    <filter id="soft-shadow" x="-20%" y="-20%" width="140%" height="140%">
      <feDropShadow dx="0" dy="12" stdDeviation="14" flood-color="#021a45" flood-opacity="0.45"/>
    </filter>
    <clipPath id="clip-tech"><circle cx="510" cy="340" r="170"/></clipPath>
    <clipPath id="clip-people"><circle cx="682" cy="340" r="170"/></clipPath>
    <clipPath id="clip-tech-people" clip-path="url(#clip-tech)"><circle cx="682" cy="340" r="170"/></clipPath>
  </defs>

  <rect class="background" width="1200" height="844" fill="url(#bg-gradient)"/>
  <rect class="circuit-texture" width="1200" height="470" fill="url(#circuit-wash)" role="img" aria-label="Faint circuit-board trace pattern across the upper background"/>

  <g class="venn" filter="url(#soft-shadow)">
    <circle class="domain domain--technology" cx="510" cy="340" r="170" fill="url(#tech-fill)"/>
    <circle class="domain domain--people" cx="682" cy="340" r="170" fill="url(#people-fill)"/>
    <circle class="domain domain--systems" cx="595" cy="487" r="170" fill="url(#systems-fill)"/>
  </g>

  <g class="overlaps">
    <circle class="overlap overlap--ui" cx="682" cy="340" r="170" fill="var(--overlap-ui)" clip-path="url(#clip-tech)"/>
    <circle class="overlap overlap--system-interface" cx="595" cy="487" r="170" fill="var(--overlap-sys)" clip-path="url(#clip-tech)"/>
    <circle class="overlap overlap--organisation" cx="595" cy="487" r="170" fill="var(--overlap-org)" clip-path="url(#clip-people)"/>
    <circle class="core" cx="595" cy="487" r="170" fill="url(#core-fill)" clip-path="url(#clip-tech-people)"/>
  </g>

  <g class="rings" fill="none" stroke="var(--ring)" stroke-width="6">
    <circle cx="510" cy="340" r="170"/>
    <circle cx="682" cy="340" r="170"/>
    <circle cx="595" cy="487" r="170"/>
  </g>

  <g class="icon-gears">
    <circle class="icon-line" cx="428" cy="268" r="14" stroke-width="7" stroke-dasharray="4.8 3.2"/>
    <circle class="icon" cx="428" cy="268" r="12"/>
    <circle cx="428" cy="268" r="5" fill="var(--tech)"/>
    <circle class="icon-line" cx="458" cy="254" r="9" stroke-width="5" stroke-dasharray="3.4 2.6"/>
    <circle class="icon" cx="458" cy="254" r="8"/>
    <circle cx="458" cy="254" r="3" fill="var(--tech)"/>
  </g>

  <g class="icon-people">
    <circle class="icon" cx="768" cy="257" r="8"/>
    <path class="icon" d="M755 282 q0-16 13-16 q13 0 13 16 z"/>
    <circle class="icon" cx="748" cy="259" r="9" stroke="var(--people)" stroke-width="2"/>
    <path class="icon" d="M731 284 q0-18 17-18 q17 0 17 18 z" stroke="var(--people)" stroke-width="2"/>
  </g>

  <g class="icon-network">
    <path class="icon-line" d="M586 529 v22 M606 529 v22 M578 551 h40 M596 551 v8 M606 545 h15"/>
    <rect class="icon" x="581" y="522" width="9" height="8"/>
    <rect class="icon" x="601" y="518" width="9" height="8"/>
    <rect class="icon" x="591" y="556" width="9" height="8"/>
    <rect class="icon" x="617" y="541" width="9" height="8"/>
  </g>

  <text class="label label--domain" x="435" y="324">Technology</text>
  <text class="label label--domain" x="760" y="324">People</text>
  <text class="label label--domain" x="595" y="587">Systems</text>

  <text class="label label--overlap" x="597" y="254">User</text>
  <text class="label label--overlap" x="597" y="274">Interface</text>
  <text class="label label--overlap" x="597" y="294">Engineering</text>

  <text class="label label--overlap" x="494" y="430">System</text>
  <text class="label label--overlap" x="494" y="450">Interface</text>
  <text class="label label--overlap" x="494" y="470">Engineering</text>

  <text class="label label--overlap" x="704" y="445">Organisation</text>
  <text class="label label--overlap" x="704" y="465">Design</text>

  <text class="label label--core" x="600" y="390">Capability</text>
</svg>
</body>
</html>
```